New Bicycle shop business card

Hi!
I'm looking for a business card for my new proffesional bike mechanics shop. This shop is only for fixing broken bikes and not selling bikes.
Peferbly a modern and sleek and modern design.
Colors: black, grey, red, white
Information:
Name: Rijwielwerkplaats Vanhoutem
Shop owner: Bart Vanhoutem & Sanne Maertens
Website: www.rijwielwerkplaats-vanhoutem.be
Email: info@rijwielwerkplaats-vanhoutem.be
Phone number: +32471902386
Street adres: Kerkweg 64
9970 Oostmoere
Slogan/shop information: Herstellingen van alle merken.
Logo: see files.
Target Market(s)
People who seek a mechanic to fix or upgrade their bikes.
Contact Information for Business Card
Information:
Website: info@rijwielwerkplaats-vanhoutem.be
9970 Oostmoere
Logo: see files.

```html
<!DOCTYPE html>
<html lang="nl">
<head>
<meta charset="utf-8">
<title>Rijwielwerkplaats Vanhoutem – Visitekaartje</title>
<link href="https://fonts.googleapis.com/css2?family=Michroma&family=Exo+2:ital,wght@0,800;1,800&display=swap" rel="stylesheet">
<style>
  :root {
    --bg: #232323;
    --card: #0d0d0d;
    --card-edge: #1a1a1a;
    --red: #e3213f;
    --white: #ffffff;
    --grey: #8a8a8a;
    --ink: #111111;
  }
  html, body {
    margin: 0;
    width: 1200px;
    height: 1200px;
    overflow: hidden;
    background: var(--bg);
  }
  .stage {
    position: relative;
    width: 1200px;
    height: 1200px;
    display: flex;
    flex-direction: column;
    align-items: center;
    justify-content: center;
    gap: 60px;
  }
  .card {
    position: relative;
    width: 880px;
    height: 500px;
    background: linear-gradient(135deg, var(--card-edge), var(--card) 60%);
    box-shadow: 0 18px 40px rgba(0,0,0,.55);
    overflow: hidden;
  }

  /* Brand name set as plain text */
  .brand {
    position: absolute;
    display: flex;
    align-items: center;
    gap: 22px;
  }
  .brand-mark {
    width: 46px;
    height: 46px;
    background: var(--red);
    flex: none;
  }
  .brand-name {
    font-family: "Michroma", sans-serif;
    font-size: 27px;
    line-height: 1.35;
    letter-spacing: 2px;
    color: var(--white);
    text-transform: uppercase;
  }

  /* Front */
  .card-front .brand {
    left: 50%;
    top: 50%;
    transform: translate(-50%, -50%);
  }

  /* Back */
  .people {
    position: absolute;
    left: 58px;
    top: 52px;
  }
  .people-names {
    font-family: "Exo 2", sans-serif;
    font-weight: 800;
    font-style: italic;
    font-size: 23px;
    color: var(--white);
    text-transform: uppercase;
    letter-spacing: .5px;
  }
  .people-role {
    font-family: "Exo 2", sans-serif;
    font-weight: 800;
    font-style: italic;
    font-size: 19px;
    color: var(--red);
    text-transform: uppercase;
    margin-top: 2px;
  }
  .contact {
    position: absolute;
    left: 58px;
    top: 210px;
    font-family: "Michroma", sans-serif;
    font-size: 17px;
    color: var(--white);
    letter-spacing: 1px;
  }
  .contact-address { margin: 0 0 18px 34px; line-height: 1.6; }
  .contact-line {
    display: flex;
    align-items: center;
    gap: 14px;
    height: 32px;
  }
  .contact-line svg { width: 20px; height: 20px; flex: none; }
  .card-back .brand {
    right: 56px;
    top: 210px;
  }
  .card-back .brand-name { font-size: 23px; }
  .tagline-band {
    position: absolute;
    left: 58px;
    right: 58px;
    bottom: 48px;
    height: 44px;
    background: var(--red);
    display: flex;
    align-items: center;
    justify-content: center;
    font-family: "Exo 2", sans-serif;
    font-weight: 800;
    font-size: 23px;
    color: var(--ink);
    text-transform: uppercase;
    letter-spacing: .5px;
  }
</style>
</head>
<body>
<main class="stage">

  <section class="card card-front" aria-label="Voorkant visitekaartje">
    <div class="brand">
      <span class="brand-mark"></span>
      <div class="brand-name">Rijwielwerkplaats<br>Vanhoutem</div>
    </div>
  </section>

  <section class="card card-back" aria-label="Achterkant visitekaartje">
    <div class="people">
      <div class="people-names">Bart Vanhoutem &amp; Sanne Maertens</div>
      <div class="people-role">Shop owner</div>
    </div>

    <div class="contact">
      <div class="contact-address">Kerkweg 64<br>9970 Oostmoere</div>
      <div class="contact-line">
        <svg viewBox="0 0 24 24" aria-hidden="true"><path fill="var(--red)" d="M6.6 10.8a15 15 0 0 0 6.6 6.6l2.2-2.2a1 1 0 0 1 1-.25 11.4 11.4 0 0 0 3.6.57 1 1 0 0 1 1 1V20a1 1 0 0 1-1 1A17 17 0 0 1 3 4a1 1 0 0 1 1-1h3.5a1 1 0 0 1 1 1c0 1.25.2 2.45.57 3.57a1 1 0 0 1-.25 1z"/></svg>
        <span>+32471902386</span>
      </div>
      <div class="contact-line">
        <svg viewBox="0 0 24 24" aria-hidden="true"><g fill="none" stroke="var(--red)" stroke-width="1.8"><circle cx="12" cy="12" r="9"/><path d="M3 12h18M12 3c3 3 3 15 0 18M12 3c-3 3-3 15 0 18"/></g></svg>
        <span>www.rijwielwerkplaats-vanhoutem.be</span>
      </div>
      <div class="contact-line">
        <svg viewBox="0 0 24 24" aria-hidden="true"><g fill="none" stroke="var(--red)" stroke-width="1.8"><rect x="3" y="5" width="18" height="14"/><path d="M3 5l9 8 9-8"/></g></svg>
        <span>info@rijwielwerkplaats-vanhoutem.be</span>
      </div>
    </div>

    <div class="brand">
      <span class="brand-mark"></span>
      <div class="brand-name">Rijwielwerkplaats<br>Vanhoutem</div>
    </div>

    <div class="tagline-band">Herstellingen van alle merken</div>
  </section>

</main>
</body>
</html>
```